IT company developing solutions for air cargo industry is looking for a new website

We are a professional IT company developing solutions for air cargo industry worldwide.

We are looking to update and completely redesign our current webpages: https://www.brimleaftech.cz/

What we like about our current pages are the animated graphics on the home page. These could stay, but not a must.

The design of the new pages should be very modern, clean, unique, creative, professional, and to make a statement. We are looking for animated graphics, cool and interesting interactions, cascading layers, etc.

Our company logo is yellow, gray and black. You don’t necessarily have to stick to this colour scheme, however the corporate colors should work well with the overal design of the web pages.
Dark mode pages are also an option.

The scope of the project would include creating a:

• Header
• Footer
• Landing page
• Navigation bar (8 tabs)
• Subpages (10)

In the first stage we are looking only for the header / footer / landing page with navigaton bar / Solutions page design.
As a second round, finalists might be asked to submit another section of the website to see their consistency in terms of the look and feel proposed for the Homepage and Solutions’ pages.
The winning designer will then complete the rest of the pages.

Attached you will find a brief for the first scope of the project. Please read the note section on slide nr. 3 carefully to understand, what we exactly are looking for to achieve.

Industry/Entity Type

Aviation

Number of Pages Required

1 page

Requirements
Must have
• See brief
Nice to have
• See brief
Should not have
• See brief

```html
<!DOCTYPE html>
<html lang="en">
<head>
<meta charset="utf-8">
<title>Brimleaf Tech – Air Cargo IT Solutions</title>
<link rel="stylesheet" href="https://fonts.googleapis.com/css2?family=Roboto:wght@400;500;700&family=Poppins:wght@400&display=swap">
<style>
:root{
  --gold:#ffc515;
  --navy:#04103a;
  --navy-deep:#020a26;
  --black:#000;
  --white:#fff;
  --muted:#d9dce6;
  --globe:#1a9dff;
}
*{box-sizing:border-box;margin:0;padding:0}
html,body{width:778px;height:1200px;overflow:hidden;background:var(--black);font-family:'Roboto',Arial,sans-serif;color:var(--white)}
.page{position:relative;width:778px;height:1200px}

.promo-bar{height:29px;background:var(--gold);color:#111;font-size:10.5px;font-weight:500;display:flex;align-items:center;justify-content:center}

.hero{position:relative;height:463px;background:radial-gradient(ellipse at 75% 35%,#0a2570 0%,var(--navy) 45%,var(--navy-deep) 100%)}
.site-header{position:absolute;top:16px;left:73px;right:72px;display:flex;align-items:center;justify-content:space-between}
.brand{display:flex;align-items:center;gap:6px;font-size:14.5px;font-weight:500;color:var(--white)}
.brand-mark{width:18px;height:18px;background:var(--gold)}
.main-nav{display:flex;gap:12px;font-size:9.6px}
.main-nav a,.footer-nav a{color:var(--white);text-decoration:none}
.caret::after{content:"";display:inline-block;margin-left:3px;border:3px solid transparent;border-top:3.5px solid var(--white);vertical-align:-1px}

.hero-copy{position:absolute;left:73px;top:154px;width:300px}
.hero-title{font-size:27.5px;font-weight:700;line-height:33.5px}
.hero-text{margin-top:16px;font-family:'Poppins',Arial,sans-serif;font-size:10.3px;line-height:20px;color:var(--white)}
.btn{display:inline-flex;align-items:center;justify-content:center;margin-top:20px;width:90px;height:35px;background:var(--gold);color:#111;font-weight:500;font-size:11px;text-decoration:none}
.globe{position:absolute;left:385px;top:120px;width:318px;height:310px;border-radius:50%;
  background:radial-gradient(circle at 50% 50%,rgba(26,157,255,.55) 0%,rgba(18,110,230,.45) 55%,rgba(0,60,160,.15) 72%,transparent 78%)}

.facts{position:relative;height:420px;background:radial-gradient(ellipse at 50% 95%,#0b0d14 0%,var(--black) 70%)}
.facts-lead{position:absolute;top:94px;left:0;right:0;text-align:center;font-size:19.5px;font-weight:700;line-height:28px}
.facts-title{position:absolute;top:166px;left:74px;font-size:16px;font-weight:700}
.fact-list{position:absolute;top:203px;left:73px;width:560px;list-style:none;display:grid;grid-template-columns:358px 1fr;row-gap:12.5px}
.fact-list li{position:relative;padding-left:16px;font-size:11px;font-weight:700;line-height:15px}
.fact-list li::before{content:"";position:absolute;left:0;top:4px;width:7px;height:7px;border-radius:50%;background:var(--white)}
.fact-list b{color:var(--gold)}

.site-footer{position:relative;height:288px;background:#050505}
.footer-brand{position:absolute;top:18px;left:0;right:0;display:flex;justify-content:center;align-items:center;gap:10px;font-size:22px;font-weight:500}
.footer-brand .brand-mark{width:34px;height:34px}
.footer-nav{position:absolute;top:71px;left:0;right:0;display:flex;justify-content:center;gap:12px;font-size:9.8px}
.contacts{position:absolute;top:114px;left:97px;right:70px;display:flex;justify-content:space-between}
.contact{display:flex;gap:17px;font-size:10px;line-height:20px}
.contact h3{font-size:10px;font-weight:500}
.icon-circle{width:29px;height:29px;border-radius:50%;background:var(--gold);display:flex;align-items:center;justify-content:center;margin-top:-2px;flex:none}
.copyright{position:absolute;top:185px;left:0;right:0;text-align:center;font-size:10px}
.copyright span{color:var(--gold)}
.social{position:absolute;top:217px;left:0;right:0;display:flex;justify-content:center;gap:7.5px}
.social a{width:19px;height:19px;border-radius:50%;background:var(--gold)}
</style>
</head>
<body>
<div class="page">
  <div class="promo-bar">Affordable IT Solutions That Revolutionize Tomorrow’s Air Cargo Today</div>

  <section class="hero">
    <header class="site-header">
      <div class="brand"><span class="brand-mark"></span>Brimleaf Tech</div>
      <nav class="main-nav">
        <a href="#">Industries</a><a href="#" class="caret">Solutions</a><a href="#">Operational Support</a><a href="#">Case Studies</a><a href="#">Testimonials</a><a href="#">News</a><a href="#" class="caret">About Us</a>
      </nav>
    </header>
    <div class="hero-copy">
      <h1 class="hero-title">Seamlessly connecting the air cargo industry from Manila to Tahiti</h1>
      <p class="hero-text">Blending decades of air cargo knowledge with end-to-end IT solutions. Whether you are an Airline, GSA, GHA, Forwarder or E-commerce Operator, our expertise can elevate your daily workflows, cutting down on expenses, time, and errors.</p>
      <a class="btn" href="#">Learn More</a>
    </div>
    <div class="globe" role="img" aria-label="Glowing digital globe wrapped in a network mesh with location pins and a plane route"></div>
  </section>

  <section class="facts">
    <h2 class="facts-lead">We are not IT tech experts attempting to do cargo! We<br>are cargo experts with programming skills!</h2>
    <h3 class="facts-title">FACTS:</h3>
    <ul class="fact-list">
      <li>Established: <b>2014</b></li>
      <li>Countries covered: <b>18</b></li>
      <li>Employees: <b>22</b></li>
      <li>Connected Clients: <b>20+</b></li>
      <li>Nr. of Annual Electronic Exchanges: <b>11,500,000 +</b></li>
      <li>Nr. of Annual AWBs: <b>350,000 +</b></li>
    </ul>
  </section>

  <footer class="site-footer">
    <div class="footer-brand"><span class="brand-mark"></span>Brimleaf Tech</div>
    <nav class="footer-nav">
      <a href="#">Industries</a><a href="#" class="caret">Solutions</a><a href="#">Operational Support</a><a href="#">Case Studies</a><a href="#">Testimonials</a><a href="#">News</a><a href="#" class="caret">About Us</a>
    </nav>
    <div class="contacts">
      <div class="contact">
        <span class="icon-circle"><svg width="10" height="10" viewBox="0 0 24 24"><path fill="#111" d="M6.6 10.8a15 15 0 0 0 6.6 6.6l2.2-2.2c.3-.3.7-.4 1-.2 1.1.4 2.3.6 3.6.6.6 0 1 .4 1 1V20c0 .6-.4 1-1 1A17 17 0 0 1 3 4c0-.6.4-1 1-1h3.5c.6 0 1 .4 1 1 0 1.3.2 2.5.6 3.6.1.3 0 .7-.2 1z"/></svg></span>
        <div><h3>PHONE:</h3><p>+420 731 408 269</p></div>
      </div>
      <div class="contact">
        <span class="icon-circle"><svg width="11" height="9" viewBox="0 0 24 18"><path fill="#111" d="M0 2l12 7 12-7V0H0zM0 5v13h24V5l-12 7z"/></svg></span>
        <div><h3>EMAIL:</h3><p>info@brimleaftech.cz</p></div>
      </div>
      <div class="contact">
        <span class="icon-circle"><svg width="8" height="11" viewBox="0 0 16 22"><path fill="#111" d="M8 0a8 8 0 0 0-8 8c0 6 8 14 8 14s8-8 8-14a8 8 0 0 0-8-8zm0 11a3 3 0 1 1 0-6 3 3 0 0 1 0 6z"/></svg></span>
        <div><h3>ADDRESS:</h3><p>VAT: CZ04859210</p><p>Kolarova 214/9</p><p>170 00 Praha 7</p></div>
      </div>
    </div>
    <p class="copyright">Copyrights@2024.<span>Brimleaf Tech</span>.All Rights Reserved</p>
    <div class="social"><a href="#" aria-label="Social link"></a><a href="#" aria-label="Social link"></a><a href="#" aria-label="Social link"></a><a href="#" aria-label="Social link"></a></div>
  </footer>
</div>
</body>
</html>
```